Lumora Activewear business card design

I need a business card designed for my activewear business. I would like to use the colours pink, purple white and blue. please see attached logo. please include (name) Harriet Welloby (phone) 0417582064 (email) hattieslumora@mailvento.com (ABN) 48715290637 . please include - Free shipping on all orders over $100

Target Market(s)

female

Contact Information for Business Card

Colors

Requirements
Must have
• I need a business card designed for my activewear business. I would like to use the colours pink, purple white and blue. please see attached logo. please include (name) Harriet Welloby (phone) 0417582064 (email) hattieslumora@mailvento.com (ABN) 48715290637 . please include - Free shipping on all orders over $100

```html
<!DOCTYPE html>
<html lang="en">
<head>
<meta charset="utf-8">
<title>Lumora Activewear – Business Card</title>
<link rel="stylesheet" href="https://fonts.googleapis.com/css2?family=Montserrat:wght@300;500;700&display=swap">
<style>
  :root {
    --backdrop: #2f2824;
    --card: #414142;
    --card-edge: #2a2a2b;
    --white: #f4f4f4;
    --pink: #e15ac4;
    --purple: #a43fc4;
    --blue: #4fa3e8;
  }
  * { box-sizing: border-box; margin: 0; padding: 0; }
  html, body {
    width: 1200px;
    height: 672px;
    overflow: hidden;
    background: var(--backdrop);
    font-family: "Montserrat", sans-serif;
  }
  .stage {
    position: relative;
    width: 1200px;
    height: 672px;
    display: flex;
    justify-content: center;
    align-items: center;
    gap: 70px;
  }
  .card {
    position: relative;
    width: 330px;
    height: 540px;
    background: var(--card);
    border-radius: 3px;
    box-shadow: 0 14px 30px rgba(0,0,0,.45), 0 0 0 1px var(--card-edge);
  }
  /* front */
  .card-front { padding: 46px 34px; }
  .holder-name {
    color: var(--white);
    font-size: 22px;
    letter-spacing: 0.5px;
    font-weight: 300;
    white-space: nowrap;
  }
  .holder-name strong { font-weight: 700; }
  .job-title {
    margin-top: 8px;
    margin-left: 18px;
    color: var(--purple);
    font-size: 13px;
    font-weight: 500;
    letter-spacing: 0.5px;
  }
  .contact-list {
    list-style: none;
    margin-top: 66px;
    margin-left: 30px;
  }
  .contact-item {
    display: flex;
    align-items: center;
    gap: 10px;
    color: var(--white);
    font-size: 14px;
    font-weight: 300;
    line-height: 1.75;
    white-space: nowrap;
  }
  .contact-icon { width: 14px; height: 14px; flex: none; }
  .contact-label {
    width: 14px;
    color: var(--pink);
    font-size: 10px;
    font-weight: 500;
    margin-right: 10px;
  }
  .brand {
    position: absolute;
    display: flex;
    align-items: center;
    gap: 10px;
  }
  .brand-dot {
    border-radius: 50%;
    background: var(--pink);
  }
  .brand-name {
    color: var(--purple);
    font-weight: 700;
    letter-spacing: 2px;
  }
  .card-front .brand { left: 58px; bottom: 48px; }
  .card-front .brand-dot { width: 24px; height: 24px; }
  .card-front .brand-name { font-size: 30px; }
  /* back */
  .card-back .brand { right: 38px; bottom: 82px; }
  .card-back .brand-dot { width: 32px; height: 32px; }
  .card-back .brand-name { font-size: 38px; }
  .shipping-note {
    position: absolute;
    left: 0;
    right: 0;
    bottom: 46px;
    text-align: center;
    color: var(--blue);
    font-size: 12px;
    font-weight: 500;
    letter-spacing: 0.5px;
  }
</style>
</head>
<body>
<main class="stage">
  <section class="card card-front" aria-label="Business card front">
    <h1 class="holder-name">HARRIET <strong>WELLOBY</strong></h1>
    <p class="job-title">JOB TITLE</p>
    <ul class="contact-list">
      <li class="contact-item">
        <svg class="contact-icon" viewBox="0 0 16 16" aria-hidden="true">
          <path fill="#e15ac4" d="M2 6c0-2 3-3 6-3s6 1 6 3v1h-3V5.5H5V7H2zM4 8h8l1 6H3zm4 1.5a2 2 0 1 0 0 4 2 2 0 0 0 0-4z"/>
        </svg>
        0417582064
      </li>
      <li class="contact-item">
        <svg class="contact-icon" viewBox="0 0 16 16" aria-hidden="true">
          <rect x="1" y="3.5" width="14" height="9" fill="#e15ac4"/>
          <path d="M1 3.5l7 5 7-5" fill="none" stroke="#414142" stroke-width="1.2"/>
        </svg>
        hattieslumora@mailvento.com
      </li>
      <li class="contact-item">
        <span class="contact-label">ABN</span>
        48715290637
      </li>
    </ul>
    <div class="brand">
      <span class="brand-dot"></span>
      <span class="brand-name">LUMORA</span>
    </div>
  </section>

  <section class="card card-back" aria-label="Business card back">
    <div class="brand">
      <span class="brand-dot"></span>
      <span class="brand-name">LUMORA</span>
    </div>
    <p class="shipping-note">Free shipping on all orders over $100</p>
  </section>
</main>
</body>
</html>
```